Creating High Performance Leadership Teams

I periodically write articles that I sent out to executive and Senior leaders. They should be reproducable in print form yet most of them will go out in pdf Format. I have attached a recent example that we did and I would like to see what you can do with the second example I have attached.

The Format should ideally fit in an A3 Format.

Target Market(s)

Executive and Senior Leaders

Industry/Entity Type

Leadership

Font styles to use
Other font styles liked:
• we often use calibri

Requirements
Must have
• Fit on a A3 paper Format, like the example I sent
Nice to have
• Should look highly professional, perhaps picutures or graphics to Support the text, a Little bit like the Maplecroft Trade Quarterly Articles (MTQ) although mine are shorter.
• You will see our Color formatting by visiting our Website, www.cortavo-insight.com

```html
<!DOCTYPE html>
<html lang="en">
<head>
<meta charset="utf-8">
<title>Creating High Performance Leadership Teams</title>
<link href="https://fonts.googleapis.com/css2?family=Carlito:ital,wght@0,400;0,700;1,400&family=Open+Sans:wght@300;600;700&display=swap" rel="stylesheet">
<style>
  :root{
    --page:#eef0f2;
    --card:#ffffff;
    --ink:#3a3d40;
    --muted:#6d7175;
    --blue:#1c5a8c;
    --title-grey:#8c9094;
    --quote-bg:#e3e6e9;
    --rule:#c9cdd1;
  }
  *{box-sizing:border-box;margin:0;padding:0}
  html,body{width:849px;height:1200px;overflow:hidden}
  body{
    position:relative;
    background:linear-gradient(180deg,#f6f7f8 0%,var(--page) 100%);
    font-family:"Carlito","Calibri",sans-serif;
    color:var(--ink);
  }
  .running-head{
    position:absolute;left:18px;top:8px;
    font-size:11px;color:var(--muted);
  }
  .insight-card{
    position:absolute;left:14px;top:32px;width:821px;height:606px;
    background:var(--card);
    border-radius:14px;
    box-shadow:0 1px 6px rgba(0,0,0,.12);
  }
  .insight-title{
    position:absolute;
    font-family:"Open Sans",sans-serif;
    line-height:1;
  }
  .insight-title .label{
    display:block;
    font-weight:300;font-size:68px;letter-spacing:1px;
    color:var(--title-grey);
  }
  .insight-title .subtitle{
    display:block;
    font-weight:700;font-size:38px;
    color:var(--blue);
    margin-top:2px;
  }
  .insight-one{left:30px;top:50px}
  .insight-two{left:440px;top:650px}
  .insight-two .label{font-size:76px}
  .insight-two .subtitle{font-size:46px}

  .photo{
    position:absolute;left:440px;top:50px;width:368px;height:162px;
    border-radius:8px;
    background:linear-gradient(135deg,#dfe3e6 0%,#b9c1c8 40%,#6e7f8d 75%,#dde1e4 100%);
  }
  .body-text{
    position:absolute;
    font-size:14.6px;line-height:18.4px;
    text-align:justify;
    hyphens:auto;
  }
  .body-text strong{font-weight:700}
  .col-one-left{left:30px;top:196px;width:380px}
  .col-one-right{left:440px;top:226px;width:368px}

  .pull-quote{
    position:absolute;left:14px;top:656px;width:398px;height:114px;
    background:var(--quote-bg);
    border-top:2px dotted var(--rule);
    border-bottom:2px dotted var(--rule);
    padding:18px 22px;
    font-family:"Open Sans",sans-serif;
    font-weight:700;font-size:16.5px;line-height:21px;
    color:var(--blue);
  }
  .col-two-left{left:18px;top:806px;width:392px}
  .col-two-right{left:440px;top:806px;width:390px}

  .copyright{
    position:absolute;right:22px;top:1178px;
    font-size:10px;color:var(--muted);
  }
</style>
</head>
<body>
  <div class="running-head">Creating High Performance Leadership Teams</div>

  <section class="insight-card">
  </section>

  <h2 class="insight-title insight-one">
    <span class="label">INSIGHT I</span>
    <span class="subtitle">Size Does Matter</span>
  </h2>

  <div class="photo" role="img" aria-label="Photo of a leadership team working together at a table with laptops"></div>

  <p class="body-text col-one-left">Let’s start with the fundamentals. Many senior leaders inherit legacies, taking over a large executive or senior leadership team with many members. Many global organizations have their functional senior leaders (CFO, COO, CIO, and CMO) as well as presidents from the respective regions combined into one team. While bringing the top leaders of an organization together may mean you can reduce the amount of executive meetings and ensure a consistent exchange of information – you can’t build an exceptional team with a group this size. It’s impossible to create an exception leadership team with 16 members – what you have is not a team but a committee, one long on discourse and short on aligned, executable action. You decide. Leaders that aim to create an exceptional leadership team waste no time in either reducing the size of the executive team or splitting off the</p>

  <p class="body-text col-one-right">function board and then having a second larger, executive group. The first is used to truly decide executive issues and the second serves as a market exchange and sounding board function. Both are useful, but <strong>only a smaller leadership team has the opportunity to be truly exceptional.</strong> What the magic number? Six to eight members in my opinion. Often a senior leader will have one “go to” person that serves as their sparring partner (often the CFO) and this can be beneficial so long as other members do not feel second-class.</p>

  <blockquote class="pull-quote">Focusing the team on activities that only it can perform for the company helps create a centre of gravity for its members</blockquote>

  <h2 class="insight-title insight-two">
    <span class="label">INSIGHT II</span>
    <span class="subtitle">Balancing Act</span>
  </h2>

  <p class="body-text col-two-left">Members of a leadership team must be able to “balance their act”. There is an inherent tension between leading an individual function and being a fully-fledged member of a leadership team. At times, there will be a conflict of interest and priorities between what is best for their function and what is best for the overall company. Recently a leader described this to me as having a foot in two camps. Exceptional leadership teams un-</p>

  <p class="body-text col-two-right">derstand this is a natural tension and address these issues with a distinct &amp; disciplined dialog. While the balancing act is ever present (even in exceptional leadership teams), <strong>creating a compelling, shared vision and developing a sense of team purpose</strong>, focusing the team on activities that only it can perform for the company helps create a centre of gravity for its members, one that enables them to balance their act.</p>

  <footer class="copyright">© 2015 Lena Hartwig, Cortavo Insight GmbH, Munich, Germany</footer>
</body>
</html>
```